Biz Card for Harrowfield Property Partners - HWPP

Harrowfield Property Partners is a commercial real estate acquisitions firm. We buy commercial property and need to raise capital from investors for each deal we buy. The vibe needs to be: give us your money, we will multiply it.
Our website: www.hrwpp-example.com
Competitors are: https://velmarholdings-example.com/, https://tribanquepartners-example.com/, http://www.ostrellecapital-example.com/
Target Market(s)
High Net Worth Individuals, Bankers, Insurance Companies, Commercial Real Estate Brokers.
Industry/Entity Type
Investment Banking
Contact Information for Business Card
Name, Title, Addess, Cell#, Office#, email, website
Requirements
Must have
- use one of our logos. See website for look and feel: www.hrwpp-example.com
Nice to have
- see website: www.hrwpp-example.com

```html
<!DOCTYPE html>
<html lang="en">
<head>
<meta charset="utf-8">
<title>Harrowfield Property Partners – Business Card</title>
<link rel="stylesheet" href="https://fonts.googleapis.com/css2?family=Montserrat:wght@400;500;600&family=Open+Sans:wght@300;800&family=Lato:wght@400&display=swap">
<style>
  :root {
    --backdrop: #b5b5b5;
    --card: #f3f3f3;
    --navy: #142b47;
    --ink: #1b2638;
    --sky-blue: #4a8fc2;
    --sky-blue-deep: #3b7fb7;
  }
  * { margin: 0; padding: 0; box-sizing: border-box; }
  html, body {
    width: 1200px; height: 900px; overflow: hidden;
    background: var(--backdrop);
  }
  .canvas { position: relative; width: 1200px; height: 900px; }

  .card {
    position: absolute;
    background: var(--card);
    overflow: hidden;
  }
  .card--front { left: 392px; top: 196px; width: 414px; height: 236px; }
  .card--back  { left: 399px; top: 496px; width: 400px; height: 229px; }

  /* Front: identity */
  .identity { position: absolute; left: 26px; top: 22px; }
  .identity__name {
    font-family: "Open Sans", sans-serif;
    font-size: 16px; line-height: 1; color: var(--ink); letter-spacing: -0.2px;
  }
  .identity__name strong { font-weight: 800; }
  .identity__name span { font-weight: 300; }
  .identity__title {
    font-family: "Montserrat", sans-serif; font-weight: 500;
    font-size: 7.5px; color: var(--ink); margin-top: 2px; letter-spacing: 0.3px;
  }
  .identity__rule {
    position: absolute; left: 26px; top: 54px; width: 105px; height: 1.5px;
    background: var(--navy);
  }
  .identity__rule::before {
    content: ""; position: absolute; left: 0; top: -0.5px; width: 18px; height: 2.5px;
    background: var(--sky-blue);
  }

  /* Front: contact list */
  .contact-list { position: absolute; left: 24px; top: 68px; list-style: none; }
  .contact-list__item {
    display: flex; align-items: center; height: 19px;
    font-family: "Montserrat", sans-serif; font-weight: 500;
    font-size: 10.5px; color: var(--ink); letter-spacing: 0.3px;
  }
  .contact-list__icon { width: 12px; height: 12px; margin-right: 10px; fill: var(--navy); }

  /* Wordmark */
  .wordmark { position: absolute; display: flex; align-items: center; }
  .wordmark__dot { border-radius: 50%; background: var(--navy); flex: none; }
  .wordmark__name {
    font-family: "Lato", sans-serif; font-weight: 400;
    color: var(--navy); text-transform: uppercase; line-height: 1.25;
  }
  .card--front .wordmark { right: 12px; top: 18px; }
  .card--front .wordmark__dot { width: 40px; height: 40px; margin-right: 8px; }
  .card--front .wordmark__name { font-size: 8.5px; letter-spacing: 2px; }

  .card--back .wordmark { left: 92px; top: 85px; }
  .card--back .wordmark__dot { width: 60px; height: 60px; margin-right: 13px; }
  .card--back .wordmark__name { font-size: 13px; letter-spacing: 3px; }

  /* Front: skyline area */
  .skyline {
    position: absolute; left: 0; bottom: 0; width: 414px; height: 60px;
    background: linear-gradient(180deg, var(--sky-blue) 0%, var(--sky-blue-deep) 100%);
  }
</style>
</head>
<body>
<main class="canvas">

  <section class="card card--front">
    <div class="identity">
      <h1 class="identity__name"><strong>YOUR</strong> <span>NAME</span></h1>
      <p class="identity__title">Co-Founder</p>
    </div>
    <div class="identity__rule"></div>

    <ul class="contact-list">
      <li class="contact-list__item">
        <svg class="contact-list__icon" viewBox="0 0 12 12"><path d="M6 0.5a4 4 0 0 0-4 4c0 3 4 7 4 7s4-4 4-7a4 4 0 0 0-4-4zm0 5.6a1.6 1.6 0 1 1 0-3.2 1.6 1.6 0 0 1 0 3.2z"/></svg>
        123 Dummy, Lorem Ipsum
      </li>
      <li class="contact-list__item">
        <svg class="contact-list__icon" viewBox="0 0 12 12"><path d="M3 1l2 2.4-1.2 1.4c.7 1.5 1.8 2.6 3.3 3.3L8.5 7 11 9l-1.2 2C5 11 1 7 1 2.2z"/></svg>
        +00 1234 5XXX 9012
      </li>
      <li class="contact-list__item">
        <svg class="contact-list__icon" viewBox="0 0 12 12"><path d="M0.5 2.5h11v7h-11z M1.5 3.3 6 6.6l4.5-3.3" fill="none" stroke="#142b47" stroke-width="1.2"/><path d="M0.5 2.5h11L6 6.5z"/></svg>
        info@email space
      </li>
      <li class="contact-list__item">
        <svg class="contact-list__icon" viewBox="0 0 12 12"><path d="M3 0.5v10l2.4-2.3 1.6 3.5 1.5-.7-1.6-3.4h3.3z"/></svg>
        www websiteaddress
      </li>
    </ul>

    <div class="wordmark">
      <span class="wordmark__dot"></span>
      <p class="wordmark__name">Harrowfield<br>Property Partners</p>
    </div>

    <div class="skyline" role="img" aria-label="Blue silhouette of a city skyline along the bottom edge of the card"></div>
  </section>

  <section class="card card--back">
    <div class="wordmark">
      <span class="wordmark__dot"></span>
      <p class="wordmark__name">Harrowfield<br>Property Partners</p>
    </div>
  </section>

</main>
</body>
</html>
```